Business Card for innovative, tech/consultant company

We are specializing in bringing together Efficiency methodology and Technology for our Business customers. We would like an astonishing business Card that matches this idea.

Target Market(s)

Businesses of medium size or more

Industry/Entity Type

Business Consultant

Contact Information for Business Card

Name, Title, personal email, www, address, phone

Font styles to use
Sans Serif

Colors
3277b5

Requirements
Must have
• - innovative, efficient design
• - good readable
• - Colors must match our logo (blue and grey)
• - the attached font (is licensed by our Company) must be used (Syntax LT)
Should not have
• overloaded

```html
<!DOCTYPE html>
<html lang="en">
<head>
<meta charset="utf-8">
<title>Corvalis Business Card</title>
<link href="https://fonts.googleapis.com/css2?family=Open+Sans:wght@400;600&family=Arimo:wght@400;700&display=swap" rel="stylesheet">
<style>
  :root {
    --page-bg: #d9d8d6;
    --card-bg: #1b1b1d;
    --accent-blue: #1e8fd6;
    --logo-grey: #8d8e90;
    --gloss-dark: #4a4b4e;
    --text-light: #f2f2f2;
    --text-muted: #c9c9cb;
  }
  * { margin: 0; padding: 0; box-sizing: border-box; }
  html, body {
    width: 1200px; height: 787px; overflow: hidden;
    background: var(--page-bg);
  }
  .canvas {
    width: 1200px; height: 787px;
    display: flex; align-items: center; justify-content: center; gap: 60px;
  }
  .card {
    width: 520px; height: 297px;
    background: var(--card-bg);
    position: relative;
    overflow: hidden;
    box-shadow: 0 6px 18px rgba(0,0,0,0.25);
    font-family: 'Arimo', Arial, sans-serif;
  }
  /* Front */
  .card-front .wordmark {
    position: absolute; left: 56px; top: 44px;
    font-family: 'Open Sans', Arial, sans-serif;
    font-weight: 400; font-size: 96px; letter-spacing: -2px; line-height: 1;
    color: var(--gloss-dark);
  }
  .card-front .web {
    position: absolute; left: 60px; top: 190px;
    font-size: 13px; letter-spacing: 4px; color: var(--text-muted);
  }
  /* Back */
  .card-back .holder { position: absolute; left: 44px; top: 40px; }
  .holder-name { color: var(--accent-blue); font-weight: 700; font-size: 17px; }
  .holder-title { color: var(--text-light); font-size: 13px; margin-top: 4px; }
  .address {
    position: absolute; left: 44px; top: 108px;
    font-style: normal;
    color: var(--text-light); font-size: 13px; line-height: 18px;
  }
  .contacts { position: absolute; left: 44px; top: 158px; list-style: none; }
  .contacts li {
    display: flex; align-items: center; gap: 10px;
    color: var(--text-light); font-size: 13px; height: 20px;
  }
  .contacts svg { width: 12px; height: 12px; flex: none; }
  .icon-fill { fill: var(--accent-blue); }
  .icon-line { fill: none; stroke: var(--accent-blue); stroke-width: 2.5; }
  .brand {
    position: absolute; right: 30px; bottom: 24px;
  }
  .brand-name {
    font-family: 'Open Sans', Arial, sans-serif;
    font-weight: 400; font-size: 60px; line-height: 1; letter-spacing: -1px;
    color: var(--logo-grey);
  }
</style>
</head>
<body>
<main class="canvas">
  <section class="card card-front" aria-label="Card front">
    <div class="wordmark">Corvalis</div>
    <div class="web">www.corvalis.com</div>
  </section>

  <section class="card card-back" aria-label="Card back">
    <div class="holder">
      <div class="holder-name">Mark Ellison</div>
      <div class="holder-title">President</div>
    </div>
    <address class="address">
      2170 Harbor Lane<br>Oak Ridge, NY 11402
    </address>
    <ul class="contacts">
      <li>
        <svg viewBox="0 0 24 24" aria-hidden="true"><path class="icon-fill" d="M6.6 10.8a15.1 15.1 0 0 0 6.6 6.6l2.2-2.2a1 1 0 0 1 1-.25 11.4 11.4 0 0 0 3.6.57 1 1 0 0 1 1 1V20a1 1 0 0 1-1 1A17 17 0 0 1 3 4a1 1 0 0 1 1-1h3.5a1 1 0 0 1 1 1c0 1.25.2 2.45.57 3.57a1 1 0 0 1-.25 1z"/></svg>
        <span>555 0182 3346</span>
      </li>
      <li>
        <svg viewBox="0 0 24 24" aria-hidden="true"><rect class="icon-line" x="2" y="5" width="20" height="14"/><path class="icon-line" d="M2 5l10 8 10-8"/></svg>
        <span>mark@corvalis.com</span>
      </li>
      <li>
        <svg viewBox="0 0 24 24" aria-hidden="true"><circle class="icon-line" cx="12" cy="12" r="9"/><path class="icon-line" d="M3 12h18M12 3c3 3 3 15 0 18M12 3c-3 3-3 15 0 18"/></svg>
        <span>www.corvalis.com</span>
      </li>
    </ul>
    <div class="brand">
      <span class="brand-name">Corvalis</span>
    </div>
  </section>
</main>
</body>
</html>
```